Letterhead Design for Law Firm that Specializes in Property Damage Litigation

We are looking for a redesign of our letterhead. Our current letterhead lists all of our current staff members and we'd like to come up with a design that does NOT list all of the staff members so that it does not need to be updated with every newly hired employee. Must be in editable format.

We are a law firm that specializes in property damage, so we need something that is professional, yet modern. The final design should use our existing logo and should use a blue color scheme (alternate colors would be gray, black, and white).

Industry/Entity Type

Legal

Colors
0054AA
0677BA
7BADD7
CADEEF
E8F1F8

```html
<!DOCTYPE html>
<html lang="en">
<head>
<meta charset="utf-8">
<title>Hartwell Crane &amp; Osgood — Letterhead</title>
<link rel="stylesheet" href="https://fonts.googleapis.com/css2?family=Carlito:wght@400;700&family=Open+Sans:wght@400;600;700&family=Roboto+Slab:wght@300;400;700&display=swap">
<style>
  :root{
    --navy:#003263;
    --blue:#33669a;
    --rule:#2f6399;
    --gray:#646464;
    --ink:#2b2b2b;
    --soft:#555;
    --icon-fill:#b9d8f5;
    --paper:#ffffff;
    --sig:#f3f6fa;
  }
  *{margin:0;padding:0;box-sizing:border-box}
  html,body{width:852px;height:1200px;overflow:hidden;background:var(--paper)}
  .letterhead{position:relative;width:852px;height:1200px;overflow:hidden;background:var(--paper);color:var(--ink);font-family:"Carlito",sans-serif}
  .graphics{position:absolute;inset:0;width:852px;height:1200px}
  .abs{position:absolute}

  .side-ribbon{left:0;top:84px;width:142px;height:373px;background:linear-gradient(170deg,var(--gray) 0%,var(--navy) 40%,var(--gray) 65%,var(--blue) 100%)}

  .firm-name{right:78px;top:104px;text-align:right;font-family:"Roboto Slab",serif;font-weight:700;font-size:31px;line-height:33px;color:var(--navy);letter-spacing:1px}
  .tagline{right:78px;top:216px;font-family:"Open Sans",sans-serif;font-weight:600;font-size:12.5px;letter-spacing:3.6px;color:var(--soft);text-transform:uppercase}
  .website{right:78px;top:238px;font-family:"Roboto Slab",serif;font-weight:300;font-size:13px;letter-spacing:3.4px;color:var(--soft)}

  .recipient{left:183px;top:339px;font-family:"Open Sans",sans-serif;color:var(--ink)}
  .recipient .label,.recipient .name{font-weight:700;font-size:14.5px;line-height:20px}
  .recipient .role{font-size:11.5px;line-height:22px}
  .recipient .company{margin-top:20px;font-weight:700;font-size:15px;line-height:20px}
  .recipient .line{font-size:15px;line-height:20px}

  .date{right:78px;top:469px;font-family:"Open Sans",sans-serif;font-weight:700;font-size:14.5px}

  .letter-body{left:182px;top:520px;width:592px;font-size:16.4px;line-height:19.7px;text-align:justify}
  .letter-body .salutation{margin-bottom:20px}
  .letter-body p{margin-bottom:19.5px}

  .signature{left:656px;top:904px;width:118px;height:40px;background:var(--sig);border-radius:4px}
  .signatory{right:78px;top:944px;text-align:right;font-family:"Open Sans",sans-serif}
  .signatory .name{font-weight:700;font-size:15px;line-height:20px}
  .signatory .role{font-size:11.5px;line-height:16px}

  .office{top:979px;font-family:"Roboto Slab",serif;color:var(--soft)}
  .office.philadelphia{left:182px}
  .office.new-jersey{left:395px}
  .office h2{font-weight:700;font-size:14.3px;color:var(--navy);letter-spacing:.3px;line-height:22px}
  .office .phones{font-weight:300;font-size:14.5px;line-height:20px;padding-bottom:8px;width:155px;border-bottom:2px solid var(--navy)}
  .office .address{font-weight:300;font-size:14.5px;line-height:17.8px;margin-top:11px;font-style:normal}
</style>
</head>
<body>
<main class="letterhead">
  <div class="abs side-ribbon" role="img" aria-label="Folded ribbon graphic in navy, blue and gray"></div>

  <svg class="graphics" viewBox="0 0 1624 2288" preserveAspectRatio="none" aria-hidden="true">
    <rect x="346" y="540" width="1129" height="3" fill="var(--rule)"/>
    <rect x="260" y="872" width="3.5" height="1148" fill="var(--rule)"/>
    <circle cx="262" cy="1960" r="40" fill="var(--icon-fill)" stroke="var(--navy)" stroke-width="4"/>
    <circle cx="262" cy="2066" r="40" fill="var(--icon-fill)" stroke="var(--navy)" stroke-width="4"/>
    <path fill="var(--navy)" d="M250,1947 l8,-4 l7,12 l-6,5 q4,9 12,13 l5,-6 l12,7 l-4,8 q-18,3 -30,-12 q-9,-12 -4,-23z"/>
    <path fill="var(--navy)" d="M262,2050 l-20,18 h6 v15 h10 v-10 h8 v10 h10 v-15 h6z"/>
    <rect x="1200" y="2043" width="424" height="109" fill="var(--gray)"/>
    <rect x="0" y="2193" width="1624" height="95" fill="var(--navy)"/>
  </svg>

  <header>
    <h1 class="abs firm-name">HARTWELL<br>CRANE &amp;<br>OSGOOD</h1>
    <div class="abs tagline">The Property Damage Attorneys</div>
    <div class="abs website">www.hcolawgroup.com</div>
  </header>

  <section class="abs recipient">
    <div class="label">TO</div>
    <div class="name">THE RECIEVER</div>
    <div class="role">Managing Director</div>
    <div class="company">Name of the Company</div>
    <div class="line">Address of the company:</div>
    <div class="line">phone number:</div>
  </section>

  <div class="abs date">Mar, 27th 2023</div>

  <article class="abs letter-body">
    <p class="salutation">Dear Sir,</p>
    <p>I know it can be a rocky road to finding the right freelancer that...Has the skills you need, someone who understands the principles of creating designs that will attract your target audience, AND who is actually motivated to work closely with you, AND That you can trust to get the job done RIGHT, the FIRST time while following your brief. I made many variations of the logo ranging from colored to the black and white version, the app on, color variations, and logo formation variations, so that you can make choice.</p>
    <p>I made research about this project especially about the jet stream dynamics, at least I grabbed a bit of the normal west-to-east jet stream where it happens to be cold and the other side where it happens to be warm. And how does it apply to the logo, so in the color of the cloud in the logo icon which is bluish, I made it to be a darker blue flowing to a warm blue, the dark shade representing cold and warm shade representing warm.</p>
    <p>The concept is actually a bright sun coming out from the cloud, and the radial patterns represents Continuous revolving of the earth as related to weather, this is a also a radial pattern that symbolizes trust, unity and quality according to logo physiology.</p>
  </article>

  <div class="abs signature" role="img" aria-label="Handwritten signature of the managing director"></div>
  <div class="abs signatory">
    <div class="name">Daniel R.Whitcombe</div>
    <div class="role">Managing Director</div>
  </div>

  <footer>
    <section class="abs office philadelphia">
      <h2>PHILADELPHIA OFFICE</h2>
      <div class="phones">215.430.7720<br>215.430.7790</div>
      <address class="address">2280 Walnut Avenue<br>Suit 840<br>Philadelphia , Pa 19107</address>
    </section>
    <section class="abs office new-jersey">
      <h2>NEW JERSEY OFFICE</h2>
      <div class="phones">856.212.4408<br>215.430.7790</div>
      <address class="address">615 Maple Ridge Road<br>Suite 310<br>Haddonfield, Nj 08033</address>
    </section>
  </footer>
</main>
</body>
</html>
```